Cocktail-Making Assistant App re-design

Ok boys and girls, here's the deal:
I have an android app which is almost complete, but needs a design overhaul.

The app is a standard cocktail-making assistant: gives you a list of cocktails and the ability to see which cocktail you can make out of those ingredients (drinks, fruit, etc) you have at home.

I've attached some general app flow, as well as detailed requirements/explanation presentation. Most of those things are just FYI, so that you know what it's about.

3 screens are the most important (main screen, cocktail view screen, ingredient view screen), meaning I will pick the design mostly based on ideas for those 3 things, with the fourth being a rather simple list (given on attached flow, third tier)
Some other screens are derived from that, with some minor changes on it, but you shouldn't care about that.

There are lots of other, non-explained things which I said nothing about only because they are (from design point of view) completely the same and would only make it seem more complicated.

I don't want to influence the colour scheme, but the app will be released under RedCedar developer name (having a light colured red cedar as a logo) so I suppose some brownish design, for example, will not really fit nicely. If you, however, have a killer which you are confident will prove me wrong, I'm looking forward to seeing it!

It should be a serious, elegant look (as opposed to cartoonish, but we are not aiming for a business look at all!), not cluttered with details, no clubbing themes, glitter and so on.

Test apk file available on request (Android 2.3+).

Edit: payment is now guaranteed
Also please note that currently, the favorite, "heart" button has a motion effect:
on click it flies out of the screen to the left (white heart) and comes back to the screen as a red heart. Take that into consideration, if it means anything to you.

Reason: Some designers are enthusiastic but will need an extra weekend to polish their ideas.

Target Market(s)

Whoever you imagine would enjoy drinking cocktails

Industry/Entity Type

Business

Requirements
Must have
• Everything is said in the provided documentation - images say more than I could possibly write here.
Nice to have
• As said, most of the icons are a nice-to-have. Only those which are critically linked to the rest of the design must be provided. More details in the docs.
Should not have
• No cartoon look, No zillion colours

```html
<!DOCTYPE html>
<html lang="en">
<head>
<meta charset="utf-8">
<title>Cocktail Assistant – Home and Search Screens</title>
<link href="https://fonts.googleapis.com/css2?family=Roboto:wght@400;500;700&display=swap" rel="stylesheet">
<style>
  :root {
    --canvas: #e4e4e4;
    --bar-black: #000000;
    --action-bar: #4b4f5a;
    --action-logo: #5f636c;
    --screen-bg: #202125;
    --tile-bg: #25272c;
    --tile-line: #1a1b1e;
    --tile-edge: #2e3036;
    --label: #b9bcc6;
    --title: #eef0f4;
    --row-text: #e2e3e6;
    --divider: #35373d;
    --thumb: #cbccce;
    --search-bg: #3a3b40;
    --search-text: #cfd0d4;
    --holo-blue: #33b5e5;
    --nav-icon: #d6d6d6;
  }
  * { box-sizing: border-box; margin: 0; padding: 0; }
  html, body { width: 1200px; height: 1000px; overflow: hidden; }
  body { background: var(--canvas); font-family: "Roboto", sans-serif; position: relative; }

  .phone { position: absolute; top: 52px; height: 896px; background: var(--screen-bg); overflow: hidden; }
  .phone--home { left: 30px; width: 537px; }
  .phone--search { left: 632px; width: 538px; }

  .status-bar { position: absolute; left: 0; right: 0; top: 0; height: 35px; background: var(--bar-black); }
  .status-bar__icons { position: absolute; right: 8px; top: 5px; display: flex; align-items: center; gap: 6px; }
  .status-bar__time { color: var(--holo-blue); font-size: 22px; line-height: 24px; }

  .action-bar { position: absolute; left: 0; right: 0; top: 35px; height: 67px; background: var(--action-bar); display: flex; align-items: center; }
  .action-bar__logo { width: 43px; height: 43px; margin-left: 19px; background: var(--action-logo); border: 1px solid #6d7179; }
  .action-bar__title { color: var(--title); font-size: 25px; margin-left: 11px; }

  .nav-bar { position: absolute; left: 0; right: 0; bottom: 0; height: 67px; background: var(--bar-black); }
  .nav-bar svg { position: absolute; top: 22px; }

  /* Home grid */
  .menu-grid { position: absolute; left: 19px; top: 122px; width: 500px; height: 616px; display: grid; grid-template-columns: 1fr 1fr; grid-template-rows: repeat(3, 1fr); border: 1px solid var(--tile-edge); background: var(--tile-line); gap: 1px; border-radius: 2px; }
  .menu-tile { background: var(--tile-bg); position: relative; }
  .menu-tile__badge { position: absolute; left: 50%; top: 30px; width: 96px; height: 96px; margin-left: -48px; border-radius: 50%; box-shadow: 0 3px 4px rgba(0,0,0,.55); display: flex; align-items: center; justify-content: center; }
  .menu-tile__label { position: absolute; left: 0; right: 0; top: 151px; text-align: center; color: var(--label); font-size: 20px; font-weight: 700; }
  .badge--shaker { background: linear-gradient(#b9d6d6, #93b0b2); }
  .badge--bar { background: linear-gradient(#7c8cbc, #5a6795); }
  .badge--cocktails { background: linear-gradient(#e0502f, #b73322); }
  .badge--favorites { background: linear-gradient(#d63e40, #a92a2f); }
  .badge--shopping { background: linear-gradient(#d3d03a, #a9a624); }
  .badge--featured { background: linear-gradient(#d8973a, #b26f23); }

  .points { position: absolute; left: 28px; top: 780px; color: var(--row-text); font-size: 22px; letter-spacing: .3px; }
  .settings-button { position: absolute; left: 467px; top: 764px; }

  /* Search screen */
  .search-field { position: absolute; left: 16px; top: 111px; width: 505px; height: 56px; background: var(--search-bg); border: 1px solid #46474d; border-radius: 2px; display: flex; align-items: center; justify-content: space-between; padding: 0 20px 0 22px; }
  .search-field__placeholder { color: var(--search-text); font-size: 22px; }
  .category-list { position: absolute; left: 21px; top: 180px; width: 497px; list-style: none; }
  .category-list__item { height: 93px; border-bottom: 1px solid var(--divider); display: flex; align-items: center; }
  .category-list__thumb { width: 60px; height: 60px; background: var(--thumb); margin-left: 5px; border-radius: 2px; }
  .category-list__name { color: var(--row-text); font-size: 24px; margin-left: 33px; }
</style>
</head>
<body>

<!-- Home screen -->
<section class="phone phone--home">
  <div class="status-bar">
    <div class="status-bar__icons">
      <svg width="22" height="22" viewBox="0 0 22 22"><path d="M4 9h4l5-5v14l-5-5H4z" fill="#9a9a9a"/><line x1="3" y1="19" x2="19" y2="3" stroke="#9a9a9a" stroke-width="2"/></svg>
      <svg width="24" height="24" viewBox="0 0 24 24"><text x="0" y="9" font-size="9" font-family="Roboto, sans-serif" font-weight="700" fill="#ccc">H</text><path d="M6 22L22 6v16z" fill="var(--holo-blue)"/></svg>
      <svg width="14" height="24" viewBox="0 0 14 24"><rect x="4" y="1" width="6" height="3" fill="var(--holo-blue)"/><rect x="1" y="3" width="12" height="20" fill="var(--holo-blue)"/></svg>
      <span class="status-bar__time">10:07</span>
    </div>
  </div>
  <header class="action-bar">
    <div class="action-bar__logo"></div>
    <h1 class="action-bar__title" style="font-weight:400">App Name</h1>
  </header>

  <nav class="menu-grid">
    <div class="menu-tile">
      <div class="menu-tile__badge badge--shaker">
        <svg width="40" height="60" viewBox="0 0 40 60"><rect x="15" y="2" width="10" height="6" rx="2" fill="#1e1f22"/><path d="M11 10h18l-2 9H13z" fill="#1e1f22"/><path d="M12 21h16l-2 36H14z" fill="#1e1f22"/></svg>
      </div>
      <span class="menu-tile__label">Shaker</span>
    </div>
    <div class="menu-tile">
      <div class="menu-tile__badge badge--bar">
        <svg width="60" height="64" viewBox="0 0 60 64"><path d="M8 62V34l5-8V14h4v12l5 8v28z" fill="#1e1f22"/><path d="M22 62V38l4-6v-8h4v8l4 6v24z" fill="#1e1f22"/><path d="M36 62V26l4-6V4h5v16l4 6v36z" fill="#1e1f22"/></svg>
      </div>
      <span class="menu-tile__label">My Bar</span>
    </div>
    <div class="menu-tile">
      <div class="menu-tile__badge badge--cocktails">
        <svg width="56" height="66" viewBox="0 0 56 66"><path d="M8 20h38L29 40v18h9v3H18v-3h9V40z" fill="#1e1f22"/><line x1="30" y1="22" x2="44" y2="4" stroke="#1e1f22" stroke-width="2"/><circle cx="40" cy="10" r="3" fill="#1e1f22"/></svg>
      </div>
      <span class="menu-tile__label">Cocktails</span>
    </div>
    <div class="menu-tile">
      <div class="menu-tile__badge badge--favorites">
        <svg width="50" height="46" viewBox="0 0 50 46"><path d="M25 44L5 24C-2 16 2 3 13 3c6 0 10 4 12 8 2-4 6-8 12-8 11 0 15 13 8 21z" fill="#1e1f22"/></svg>
      </div>
      <span class="menu-tile__label">Favorites</span>
    </div>
    <div class="menu-tile">
      <div class="menu-tile__badge badge--shopping">
        <svg width="52" height="46" viewBox="0 0 52 46"><path d="M20 18V6a6 6 0 0 1 12 0v12" fill="none" stroke="#1e1f22" stroke-width="4"/><rect x="2" y="18" width="48" height="6" fill="#1e1f22"/><path d="M6 26h40l-4 18H10z" fill="#1e1f22"/><g stroke="#bdbb30" stroke-width="2"><line x1="16" y1="30" x2="16" y2="40"/><line x1="22" y1="30" x2="22" y2="40"/><line x1="28" y1="30" x2="28" y2="40"/><line x1="34" y1="30" x2="34" y2="40"/></g></svg>
      </div>
      <span class="menu-tile__label">Shopping List</span>
    </div>
    <div class="menu-tile">
      <div class="menu-tile__badge badge--featured">
        <svg width="50" height="62" viewBox="0 0 50 62"><path d="M14 32L6 54l8-3 4 8 7-22zM36 32l8 22-8-3-4 8-7-22z" fill="#1e1f22"/><circle cx="25" cy="22" r="19" fill="#1e1f22"/><circle cx="25" cy="22" r="11" fill="none" stroke="#c6832e" stroke-width="2"/></svg>
      </div>
      <span class="menu-tile__label">Featured</span>
    </div>
  </nav>

  <p class="points">POINTS : 100</p>
  <svg class="settings-button" width="54" height="54" viewBox="0 0 54 54">
    <circle cx="27" cy="27" r="24.5" fill="none" stroke="#c9cbd6" stroke-width="2.5"/>
    <g fill="#c9cbd6" transform="translate(27 27)">
      <rect x="-3.5" y="-16" width="7" height="32" rx="1"/>
      <rect x="-3.5" y="-16" width="7" height="32" rx="1" transform="rotate(45)"/>
      <rect x="-3.5" y="-16" width="7" height="32" rx="1" transform="rotate(90)"/>
      <rect x="-3.5" y="-16" width="7" height="32" rx="1" transform="rotate(135)"/>
      <circle r="11"/>
    </g>
    <circle cx="27" cy="27" r="5" fill="var(--screen-bg)"/>
  </svg>

  <div class="nav-bar">
    <svg style="left:88px" width="48" height="24" viewBox="0 0 48 24"><path d="M10 4L3 10l7 6M3 10h34a7 7 0 0 1 0 14H20" fill="none" stroke="var(--nav-icon)" stroke-width="2.5"/></svg>
    <svg style="left:242px" width="52" height="26" viewBox="0 0 52 26"><path d="M2 24V12L26 2l24 10v12z" fill="none" stroke="var(--nav-icon)" stroke-width="2.5"/></svg>
    <svg style="left:402px" width="50" height="24" viewBox="0 0 50 24"><rect x="2" y="9" width="38" height="13" fill="none" stroke="var(--nav-icon)" stroke-width="2.5"/><path d="M8 5h36v12" fill="none" stroke="var(--nav-icon)" stroke-width="2.5"/></svg>
  </div>
</section>

<!-- Search screen -->
<section class="phone phone--search">
  <div class="status-bar">
    <div class="status-bar__icons">
      <svg width="22" height="22" viewBox="0 0 22 22"><path d="M4 9h4l5-5v14l-5-5H4z" fill="#9a9a9a"/><line x1="3" y1="19" x2="19" y2="3" stroke="#9a9a9a" stroke-width="2"/></svg>
      <svg width="24" height="24" viewBox="0 0 24 24"><text x="0" y="9" font-size="9" font-family="Roboto, sans-serif" font-weight="700" fill="#ccc">H</text><path d="M6 22L22 6v16z" fill="var(--holo-blue)"/></svg>
      <svg width="14" height="24" viewBox="0 0 14 24"><rect x="4" y="1" width="6" height="3" fill="var(--holo-blue)"/><rect x="1" y="3" width="12" height="20" fill="var(--holo-blue)"/></svg>
      <span class="status-bar__time">10:07</span>
    </div>
  </div>
  <header class="action-bar">
    <div class="action-bar__logo"></div>
    <h1 class="action-bar__title" style="font-weight:400">Cocktail Search</h1>
  </header>

  <div class="search-field">
    <span class="search-field__placeholder">Search</span>
    <svg width="32" height="32" viewBox="0 0 32 32"><circle cx="12" cy="12" r="8.5" fill="none" stroke="#e6e6e8" stroke-width="3.5"/><line x1="18" y1="18" x2="28" y2="28" stroke="#e6e6e8" stroke-width="5" stroke-linecap="round"/></svg>
  </div>

  <ul class="category-list">
    <li class="category-list__item"><span class="category-list__thumb"></span><span class="category-list__name">All</span></li>
    <li class="category-list__item"><span class="category-list__thumb"></span><span class="category-list__name">Cocktails</span></li>
    <li class="category-list__item"><span class="category-list__thumb"></span><span class="category-list__name">Party Drinks</span></li>
    <li class="category-list__item"><span class="category-list__thumb"></span><span class="category-list__name">Shots</span></li>
    <li class="category-list__item"><span class="category-list__thumb"></span><span class="category-list__name">Milky Drinks</span></li>
    <li class="category-list__item"><span class="category-list__thumb"></span><span class="category-list__name">Other</span></li>
  </ul>

  <div class="nav-bar">
    <svg style="left:88px" width="48" height="24" viewBox="0 0 48 24"><path d="M10 4L3 10l7 6M3 10h34a7 7 0 0 1 0 14H20" fill="none" stroke="var(--nav-icon)" stroke-width="2.5"/></svg>
    <svg style="left:242px" width="52" height="26" viewBox="0 0 52 26"><path d="M2 24V12L26 2l24 10v12z" fill="none" stroke="var(--nav-icon)" stroke-width="2.5"/></svg>
    <svg style="left:402px" width="50" height="24" viewBox="0 0 50 24"><rect x="2" y="9" width="38" height="13" fill="none" stroke="var(--nav-icon)" stroke-width="2.5"/><path d="M8 5h36v12" fill="none" stroke="var(--nav-icon)" stroke-width="2.5"/></svg>
  </div>
</section>

</body>
</html>
```